Box for Colorado based custom buckle and belt company

We are looking to design a box to be used to hold belts that will be delivered through Brellix's QTR program. It should have a rustic/western feel (potentially as basic as simulated mountains) and include our company's name (R&P Clasps), website (www.randpclasps.example). There needs to be a place to attach a sticker containing a SKU on the back or side of the box.

Target Market(s)

Primary customers will be men. Our products are on the more expensive side (e.g., $100-350 for a belt).

Most customers will consider themselves to be "weekend cowboys." Someone who enjoys the western ideas, but does not live then 7 days a week.

Industry/Entity Type

Clothing

Font styles to use
Serif

Requirements
Must have
• -Company Name: R&P Clasps
• -Website: www.randpclasps.example
• -Contact info: walt@randpclasps.example and (800) 555-0192
Should not have
• Overly complicated. Would prefer clean and simple.

```html
<!DOCTYPE html>
<html lang="en">
<head>
<meta charset="utf-8">
<title>R&amp;P Clasps – Belt Mailer Box Dieline</title>
<link rel="stylesheet" href="https://fonts.googleapis.com/css2?family=Sorts+Mill+Goudy:ital@0;1&display=swap">
<style>
  :root {
    --paper: #ffffff;
    --matte-black: #000000;
    --gloss-cream: #efe6c9;
    --gloss-tan: #8c7a5a;
    --fold-line: #5a1212;
    --cut-line: #0f2a3a;
    --legend-ink: #222222;
  }
  html, body {
    margin: 0;
    padding: 0;
    background: var(--paper);
    overflow: hidden;
  }
  .canvas {
    width: 1200px;
    height: 1091px;
    position: relative;
    overflow: hidden;
  }
  .dieline { display: block; }
  .panel { fill: var(--matte-black); }
  .fold { fill: none; stroke: var(--fold-line); stroke-width: 1; }
  .cut { fill: none; stroke: var(--cut-line); stroke-width: 1; }
  .type {
    font-family: "Sorts Mill Goudy", Georgia, serif;
    fill: var(--gloss-cream);
  }
  .type--italic { font-style: italic; }
  .type--centered { text-anchor: middle; }
  .wordmark-lid { font-size: 86px; }
  .wordmark-front { font-size: 44px; }
  .wordmark-side { font-size: 22px; fill: var(--gloss-tan); }
  .side-url { font-size: 14px; }
  .back-info { font-size: 13.5px; }
  .sku-area { fill: none; stroke: var(--gloss-cream); stroke-width: 1.5; }
  .sku-label { font-size: 15px; }
  .legend-text {
    font-family: "Sorts Mill Goudy", Georgia, serif;
    fill: var(--legend-ink);
    font-size: 21px;
    text-anchor: middle;
  }
  .swatch--cream { fill: var(--gloss-cream); }
  .swatch--tan { fill: var(--gloss-tan); }
  .swatch--black { fill: var(--matte-black); }
</style>
</head>
<body>
<div class="canvas">
<svg class="dieline" width="1200" height="1091" viewBox="0 0 1500 1364" xmlns="http://www.w3.org/2000/svg">

  <!-- Top tuck flap -->
  <rect class="panel" x="518" y="40" width="464" height="160"/>
  <!-- Top dust flaps -->
  <path class="panel" d="M336 58 H518 V200 H385 L330 172 V64 Z"/>
  <path class="panel" d="M982 58 H1164 Q1170 58 1170 64 V172 L1115 200 H982 Z"/>

  <!-- Left outer side flap -->
  <path class="panel" d="M243 182 H385 V625 H243 Q213 625 213 595 V462 L205 452 V348 L213 340 V212 Q213 182 243 182 Z"/>
  <!-- Right outer side flap -->
  <path class="panel" d="M1115 182 H1257 Q1287 182 1287 212 V340 L1295 348 V452 L1287 462 V595 Q1287 625 1257 625 H1115 Z"/>

  <!-- Side walls and base -->
  <rect class="panel" x="380" y="192" width="740" height="420"/>

  <!-- Back wall band -->
  <rect class="panel" x="525" y="605" width="450" height="145"/>
  <!-- Bottom dust flaps -->
  <path class="panel" d="M330 628 H528 V748 H330 Q325 748 325 742 V642 L380 628 Z"/>
  <path class="panel" d="M972 628 H1170 Q1176 628 1176 634 V742 Q1176 748 1170 748 H972 Z"/>

  <!-- Lid -->
  <path class="panel" d="M470 748 H1030 Q1112 748 1112 830 V1100 Q1112 1160 1050 1165 H450 Q388 1160 388 1100 V830 Q388 748 470 748 Z"/>
  <!-- Front tuck -->
  <path class="panel" d="M410 1152 H1090 Q1120 1152 1120 1182 Q1120 1322 960 1322 H540 Q380 1322 380 1182 Q380 1152 410 1152 Z"/>

  <!-- Fold lines -->
  <path class="fold" d="M535 58 V195 M965 58 V195 M535 195 H965"/>
  <path class="fold" d="M370 195 V610 M385 195 V610 M525 195 V610 M975 195 V610 M1115 195 V610 M1130 195 V610"/>
  <path class="fold" d="M525 610 H975 M528 610 V748 M972 610 V748 M528 748 H972"/>
  <path class="fold" d="M543 748 V1168 M957 748 V1168 M543 1168 H957 M530 1168 V1305 M970 1168 V1305"/>

  <!-- Cut lines -->
  <path class="cut" d="M255 198 H370 V610 H255 Q230 610 230 585 V223 Q230 198 255 198 Z"/>
  <path class="cut" d="M1130 198 H1245 Q1270 198 1270 223 V585 Q1270 610 1245 610 H1130 Z"/>
  <rect class="cut" x="526" y="350" width="16" height="104" rx="8"/>
  <rect class="cut" x="958" y="350" width="16" height="104" rx="8"/>
  <path class="cut" d="M543 760 L470 772 Q405 780 405 850 V1095 Q405 1158 470 1160 L543 1164"/>
  <path class="cut" d="M957 760 L1030 772 Q1095 780 1095 850 V1095 Q1095 1158 1030 1160 L957 1164"/>
  <path class="cut" d="M530 1170 H430 Q398 1170 398 1200 Q420 1300 530 1305 M970 1170 H1070 Q1102 1170 1102 1200 Q1080 1300 970 1305"/>

  <!-- Left side wall -->
  <text class="type wordmark-side type--centered" transform="translate(450 403) rotate(-90)">R&amp;P</text>
  <text class="type side-url type--centered" transform="translate(482 398) rotate(-90)">randpclasps.example</text>

  <!-- Right side wall -->
  <text class="type wordmark-side type--centered" transform="translate(1050 403) rotate(90)">R&amp;P</text>
  <text class="type side-url type--centered" transform="translate(1017 408) rotate(90)">randpclasps.example</text>

  <!-- Back wall: contact info and sticker area (reads upright once folded) -->
  <g transform="rotate(180 750 679)">
    <text class="type back-info type--centered" x="680" y="642">R&amp;P Clasps</text>
    <text class="type back-info type--centered" x="680" y="660">randpclasps.example</text>
    <text class="type back-info type--italic type--centered" x="680" y="694">Any Questions?  Please contact us at:</text>
    <text class="type back-info type--centered" x="680" y="711">walt@randpclasps.example</text>
    <text class="type back-info type--centered" x="680" y="728"><tspan font-style="italic">or by phone at:</tspan> (800) 555-0192</text>
    <rect class="sku-area" x="828" y="629" width="103" height="103"/>
    <text class="type sku-label type--centered" x="879" y="664">Bar Code</text>
    <text class="type sku-label type--centered" x="879" y="686">&amp; SKU #</text>
    <text class="type sku-label type--centered" x="879" y="708">Area</text>
  </g>

  <!-- Lid wordmark -->
  <text class="type wordmark-lid type--centered" x="750" y="982">R&amp;P Clasps</text>

  <!-- Front tuck wordmark -->
  <text class="type wordmark-front type--centered" x="750" y="1250">Rowan &amp; Pike</text>

  <!-- Print legend -->
  <text class="legend-text" x="195" y="1125">Gloss Varnish Logos and Type</text>
  <text class="legend-text" x="195" y="1148">on Matte Black Background</text>
  <text class="legend-text" x="134" y="1185">Gloss Varnish</text>
  <text class="legend-text" x="275" y="1185">Matte Black</text>
  <rect class="swatch--cream" x="62" y="1197" width="67" height="67"/>
  <rect class="swatch--tan" x="139" y="1197" width="68" height="67"/>
  <rect class="swatch--black" x="242" y="1197" width="67" height="67"/>
</svg>
</div>
</body>
</html>
```